Real Estate Investor needs awesome business card design

I invest in real estate, focused on multi-family properties, and I need a business card to hand out to potential partners. I prefer simple, clean designs, but it needs to stand out, so I'd like there to be a bit of red in the design as well.

It should include this information:

Front
Dallin Pecksworth
Real Estate Investor
Direct phone: 502-867-3394
Email: dallinhpecksworth@quillmail.example
Headshot (Picture), I've uploaded a few, just pick the one you think looks best with your design. You can remove the background from the headshot image if it looks better.

Back
The back of the card's design should flow and be congruent with the front. On the back I want to put an inspirational quote or question. There will be different ones depending on the card, so I'll need the original file so I can edit it in the end.

For now, use “The Pessimist Sees Difficulty In Every Opportunity. The Optimist Sees The Opportunity In Every Difficulty.” -Barnaby Ellsworth

Target Market(s)

Investors

Industry/Entity Type

Real Estate

Contact Information for Business Card

Front
Dallin Pecksworth
Real Estate Investor

Back
The back of the card's design should flow and be congruent with the front. On the back I want to put an inspirational quote or question. There will be different ones depending on the card, so I'll need the original file so I can edit it in the end. I've uploaded some EXAMPLES of business cards with quotes on them. Don't copy but feel free to use them as inspiration.

The design will be printed on "ZIB sized" business cards
1039 x 697 pixels
with rounded corners

Font styles to use
Serif
Decorative
Script

Colors
ec1f27

Requirements
Must have
• Headshot, name, and other information in it.
• 1039 x 697 pixels
• Rounded corners
• Clean design that pops. I'm open to see any color background, including black.
• Headshots can be located here: https://www.filecrate.example/sh/8kd2wq7mzt31hvx/BBQTXP4ruf9LmQ0KhcvWx7b?dl=0
Nice to have
• It would be awesome if the design included a personal signature or monogram, but if not I'll get a personal logo developed later and the card redesigned if I think it needs it.
Should not have
• Cluttered design

```html
<!DOCTYPE html>
<html lang="en">
<head>
<meta charset="utf-8">
<title>Dallin Pecksworth — Business Card</title>
<link rel="stylesheet" href="https://fonts.googleapis.com/css2?family=Open+Sans:wght@400;600&family=Roboto+Slab:wght@400;700&display=swap">
<style>
  :root {
    --backdrop: #5b4a3c;
    --card-white: #ffffff;
    --card-slate: #22323a;
    --photo-dark: #131e24;
    --photo-mid: #1e2d35;
    --photo-warm: #8a6a58;
    --photo-hair: #5a4636;
    --accent-red: #ec1f27;
    --ink: #1d2a33;
    --ink-soft: #3a3f44;
    --quote-text: #ffffff;
  }
  * { box-sizing: border-box; margin: 0; padding: 0; }
  html, body { width: 1200px; height: 987px; overflow: hidden; }
  body {
    position: relative;
    background: var(--backdrop);
    font-family: "Open Sans", Arial, sans-serif;
  }
  .card {
    position: absolute;
    left: 307px;
    width: 586px;
    box-shadow: 0 2px 6px rgba(0,0,0,0.35);
    overflow: hidden;
  }
  .card-front { top: 103px; height: 394px; background: var(--card-white); }
  .card-back { top: 520px; height: 392px; background: var(--card-slate); }

  .headshot {
    position: absolute; left: 0; top: 0; width: 100%; height: 305px;
    background:
      radial-gradient(ellipse 70px 100px at 27% 48%, rgba(138,106,88,0.85) 0%, rgba(138,106,88,0.35) 60%, rgba(138,106,88,0) 100%),
      radial-gradient(ellipse 80px 50px at 27% 16%, rgba(90,70,54,0.7) 0%, rgba(90,70,54,0) 100%),
      radial-gradient(ellipse 150px 70px at 24% 105%, #0d151a 0%, rgba(13,21,26,0) 100%),
      radial-gradient(ellipse at 60% 40%, var(--photo-mid) 0%, var(--photo-dark) 85%);
  }
  .accent-rule {
    position: absolute; left: 0; top: 305px; width: 100%; height: 3px;
    background: var(--accent-red);
  }
  .identity { position: absolute; left: 29px; top: 324px; color: var(--ink); }
  .identity .name { font-size: 21px; font-weight: 600; line-height: 1.1; }
  .identity .role { font-size: 15.5px; color: var(--ink-soft); margin-top: 4px; margin-left: 2px; }

  .contact { position: absolute; right: 34px; top: 328px; color: var(--ink-soft); font-size: 15.5px; }
  .contact li { list-style: none; display: flex; justify-content: flex-end; align-items: center; gap: 9px; height: 23px; }
  .contact svg { width: 14px; height: 14px; fill: var(--ink); }

  .quote { position: absolute; left: 102px; top: 138px; color: var(--quote-text); font-family: "Roboto Slab", Rockwell, Georgia, serif; }
  .quote blockquote { font-size: 18.5px; line-height: 27px; text-transform: uppercase; position: relative; }
  .quote .mark { position: absolute; width: 36px; height: 24px; fill: var(--quote-text); }
  .quote .mark-open { left: -47px; top: -10px; }
  .quote .mark-close { position: relative; display: inline-block; vertical-align: top; margin-left: 4px; top: 2px; }
  .quote .author { font-weight: 700; font-size: 15px; text-transform: uppercase; margin-top: 10px; letter-spacing: 0.2px; }
</style>
</head>
<body>
  <section class="card card-front">
    <div class="headshot" role="img" aria-label="Headshot portrait of Dallin Pecksworth on a dark slate background"></div>
    <div class="accent-rule"></div>
    <div class="identity">
      <p class="name">DALLIN PECKSWORTH</p>
      <p class="role">Real Estate Investor</p>
    </div>
    <ul class="contact">
      <li>502-867-3394
        <svg viewBox="0 0 24 24" aria-hidden="true"><path d="M6.6 10.8c1.4 2.8 3.8 5.1 6.6 6.6l2.2-2.2c.3-.3.7-.4 1-.2 1.1.4 2.3.6 3.6.6.6 0 1 .4 1 1V20c0 .6-.4 1-1 1C10.6 21 3 13.4 3 4c0-.6.4-1 1-1h3.5c.6 0 1 .4 1 1 0 1.3.2 2.5.6 3.6.1.3 0 .7-.2 1L6.6 10.8z"/></svg>
      </li>
      <li>dallinhpecksworth@quillmail.example
        <svg viewBox="0 0 24 24" aria-hidden="true"><path d="M2 5h20v2l-10 6L2 7z"/><path d="M2 9l10 6 10-6v10H2z"/></svg>
      </li>
    </ul>
  </section>

  <section class="card card-back">
    <figure class="quote">
      <blockquote>
        <svg class="mark mark-open" viewBox="0 0 36 24" aria-hidden="true">
          <path d="M11 0C5 3 1 9 1 16v8h10V14H6c0-4 3-8 7-11z"/>
          <path d="M30 0c-6 3-10 9-10 16v8h10V14h-5c0-4 3-8 7-11z"/>
        </svg>
        The pessimist sees difficulty<br>
        in every opportunity.<br>
        The optimist sees the opportunity<br>
        in every difficulty.<svg class="mark mark-close" viewBox="0 0 36 24" aria-hidden="true">
          <path d="M5 24c6-3 10-9 10-16V0H5v10h5c0 4-3 8-7 11z"/>
          <path d="M24 24c6-3 10-9 10-16V0H24v10h5c0 4-3 8-7 11z"/>
        </svg>
      </blockquote>
      <figcaption class="author">Barnaby Ellsworth</figcaption>
    </figure>
  </section>
</body>
</html>
```